Etiketten für Imkerei
Zielgruppe
Wir sind eine Imkerei in München. Die Zielgrppe sind Menschen, die lokale Produkte wertschätzen, beim Produzenten gern direkt und auf Märkten einkaufen.
Hallo,
wir benötigen ein universelles Design für Honiggläser-Etiketten, das für verschiedene Sorten verwendet werden kann. Das vorhanden Logo soll im Design aufgenommen werden. Im Logo reicht der Name: Imkerei-Brunntal.

```html
<!DOCTYPE html>
<html lang="de">
<head>
<meta charset="utf-8">
<title>Honig Etiketten – Imkerei Brunntal</title>
<link href="https://fonts.googleapis.com/css2?family=Mulish:wght@300;400;600;700&family=Kalam:wght@400&display=swap" rel="stylesheet">
<style>
  :root{
    --bg:#eceef0;
    --white:#ffffff;
    --ink:#3a3a3a;
    --summer-body:#f0b000; --summer-stripe:#fdd000; --summer-word:#ffc61a; --summer-tag:#e0301e;
    --spring-body:#a5cc52; --spring-stripe:#7ebf2a; --spring-word:#8fc23a; --spring-tag:#f4e23a;
    --forest-body:#5a2a28; --forest-stripe:#c4201f; --forest-word:#d02020; --forest-tag:#f4d51a;
  }
  html,body{margin:0;padding:0;width:1200px;height:689px;overflow:hidden;background:var(--bg);}
  .canvas{position:relative;width:1200px;height:689px;}
  .label{position:absolute;top:225px;width:330px;height:240px;overflow:hidden;}
  .label svg{position:absolute;inset:0;width:330px;height:240px;display:block;}
  .label--summer{left:60px;--body:var(--summer-body);--stripe:var(--summer-stripe);--word:var(--summer-word);--tag:var(--summer-tag);}
  .label--spring{left:435px;--body:var(--spring-body);--stripe:var(--spring-stripe);--word:var(--spring-word);--tag:var(--spring-tag);}
  .label--forest{left:810px;--body:var(--forest-body);--stripe:var(--forest-stripe);--word:var(--forest-word);--tag:var(--forest-tag);}
  .fill-body{fill:var(--body);} .fill-stripe{fill:var(--stripe);} .fill-white{fill:var(--white);}
  .brand{position:absolute;top:28px;left:0;width:100%;display:flex;justify-content:center;align-items:center;gap:6px;
    font-family:"Mulish",sans-serif;font-weight:600;font-size:13px;color:var(--ink);}
  .brand__mark{width:14px;height:14px;border:1.5px solid var(--ink);box-sizing:border-box;}
  .content{position:absolute;left:38px;width:242px;top:0;height:240px;}
  .tagline{position:absolute;top:110px;left:0;width:100%;text-align:center;font-family:"Mulish",sans-serif;
    font-weight:600;font-size:12px;line-height:14px;color:var(--tag);}
  .tagline small{font-size:8px;}
  .product{position:absolute;top:126px;left:0;width:100%;text-align:center;font-family:"Mulish",sans-serif;
    font-weight:400;font-size:56px;line-height:56px;letter-spacing:3px;color:var(--word);}
  .variety{position:absolute;top:168px;left:0;width:100%;text-align:center;font-family:"Kalam",cursive;
    font-size:19px;line-height:24px;color:var(--white);transform:rotate(-2deg);}
  .maker{position:absolute;top:210px;left:0;width:100%;text-align:center;font-family:"Mulish",sans-serif;
    font-weight:300;font-size:11px;line-height:14px;color:var(--white);letter-spacing:.3px;}
  .info{position:absolute;top:124px;left:284px;width:44px;font-family:"Mulish",sans-serif;font-size:5.5px;
    line-height:1.4;color:var(--ink);white-space:nowrap;}
  .info__origin{margin-top:12px;font-weight:700;}
</style>
</head>
<body>
<div class="canvas">

  <!-- Sommertracht -->
  <div class="label label--summer">
    <svg viewBox="0 0 330 240" aria-hidden="true">
      <rect class="fill-white" width="330" height="240"/>
      <path class="fill-body" d="M0 75 Q80 66 165 80 Q250 70 330 62 V240 H0 Z"/>
      <rect class="fill-stripe" x="0" y="60" width="38" height="180"/>
      <rect class="fill-stripe" x="280" y="60" width="50" height="180"/>
      <g class="fill-white">
        <path d="M0 60 H330 V62 Q250 70 165 80 Q80 66 0 75 Z"/>
        <path d="M17 70 h6 v30 a3 3 0 0 1 -6 0 Z"/>
        <path d="M27 70 h5 v18 a2.5 2.5 0 0 1 -5 0 Z"/>
        <path d="M216 76 h7 v26 a3.5 3.5 0 0 1 -7 0 Z"/>
        <path d="M229 74 h5 v16 a2.5 2.5 0 0 1 -5 0 Z"/>
        <path d="M292 66 h6 v38 a3 3 0 0 1 -6 0 Z"/>
      </g>
      <rect x="0" y="190" width="38" height="50" fill="var(--body)" opacity=".35" role="img" aria-label="Gräser-Illustration"/>
    </svg>
    <div class="brand"><span class="brand__mark"></span>Imkerei-Brunntal</div>
    <div class="content">
      <div class="tagline">lokal <small>&amp;</small> natürlich</div>
      <div class="product">HONIG</div>
      <div class="variety">Sommertracht</div>
      <div class="maker">Imkerei Brunntal</div>
    </div>
    <div class="info">IMKEREI<br>BRUNNTAL<br>Tobrekweg 7<br>85400<br>Brunntal<br>honig-bt.de<div class="info__origin">Deutscher<br>Bienenhonig</div></div>
  </div>

  <!-- Frühlingsblüten -->
  <div class="label label--spring">
    <svg viewBox="0 0 330 240" aria-hidden="true">
      <rect class="fill-white" width="330" height="240"/>
      <path class="fill-body" d="M0 75 Q80 66 165 80 Q250 70 330 62 V240 H0 Z"/>
      <rect class="fill-stripe" x="0" y="60" width="38" height="180"/>
      <rect class="fill-stripe" x="280" y="60" width="50" height="180"/>
      <g class="fill-white">
        <path d="M0 60 H330 V62 Q250 70 165 80 Q80 66 0 75 Z"/>
        <path d="M17 70 h6 v30 a3 3 0 0 1 -6 0 Z"/>
        <path d="M27 70 h5 v18 a2.5 2.5 0 0 1 -5 0 Z"/>
        <path d="M216 76 h7 v26 a3.5 3.5 0 0 1 -7 0 Z"/>
        <path d="M229 74 h5 v16 a2.5 2.5 0 0 1 -5 0 Z"/>
        <path d="M292 66 h6 v38 a3 3 0 0 1 -6 0 Z"/>
      </g>
      <rect x="0" y="190" width="38" height="50" fill="var(--body)" opacity=".35" role="img" aria-label="Gräser-Illustration"/>
    </svg>
    <div class="brand"><span class="brand__mark"></span>Imkerei-Brunntal</div>
    <div class="content">
      <div class="tagline">lokal <small>&amp;</small> natürlich</div>
      <div class="product">HONIG</div>
      <div class="variety">Frühlingsblüten</div>
      <div class="maker">Imkerei Brunntal</div>
    </div>
    <div class="info">IMKEREI<br>BRUNNTAL<br>Tobrekweg 7<br>85400<br>Brunntal<br>honig-bt.de<div class="info__origin">Deutscher<br>Bienenhonig</div></div>
  </div>

  <!-- Wald -->
  <div class="label label--forest">
    <svg viewBox="0 0 330 240" aria-hidden="true">
      <rect class="fill-white" width="330" height="240"/>
      <path class="fill-body" d="M0 75 Q80 66 165 80 Q250 70 330 62 V240 H0 Z"/>
      <rect class="fill-stripe" x="0" y="60" width="38" height="180"/>
      <rect class="fill-stripe" x="280" y="60" width="50" height="180"/>
      <g class="fill-white">
        <path d="M0 60 H330 V62 Q250 70 165 80 Q80 66 0 75 Z"/>
        <path d="M17 70 h6 v30 a3 3 0 0 1 -6 0 Z"/>
        <path d="M27 70 h5 v18 a2.5 2.5 0 0 1 -5 0 Z"/>
        <path d="M216 76 h7 v26 a3.5 3.5 0 0 1 -7 0 Z"/>
        <path d="M229 74 h5 v16 a2.5 2.5 0 0 1 -5 0 Z"/>
        <path d="M292 66 h6 v38 a3 3 0 0 1 -6 0 Z"/>
      </g>
      <rect x="0" y="190" width="38" height="50" fill="var(--body)" opacity=".35" role="img" aria-label="Gräser-Illustration"/>
    </svg>
    <div class="brand"><span class="brand__mark"></span>Imkerei-Brunntal</div>
    <div class="content">
      <div class="tagline">lokal <small>&amp;</small> natürlich</div>
      <div class="product">HONIG</div>
      <div class="variety">Wald</div>
      <div class="maker">Imkerei Brunntal</div>
    </div>
    <div class="info">IMKEREI<br>BRUNNTAL<br>Tobrekweg 7<br>85400<br>Brunntal<br>honig-bt.de<div class="info__origin">Deutscher<br>Bienenhonig</div></div>
  </div>

</div>
</body>
</html>
```